A website serving business owners or those wishing to become business owners.

A website serving those in the service industry or would like to get started with their own business. From business licensing , marketing, business loans, and much more.

We offer business incubation services as well as further growth assistance.

Including, but not limited to...

marketing
websites
seo
brindle ads
social media ads
logos
business licensing assistance
customer acquisition and ongoing coordination
1. scheduling
2 customer support
3.coordination between business owners and clients

Cleaning training program/courses.

Target Market(s)

Hispanic folks looking to start or grow their cleaning company.

Industry/Entity Type

business incubation and growth support.

Coding

Coded - Design and coding required

Font styles to use
Sans Serif

Requirements
Must have
• wordpress, custom design
Nice to have
• something similar to this .... https://www.tallvesper.com/
Should not have
• no predesigned themes, no third party templates

```html
<!DOCTYPE html>
<html lang="en">
<head>
<meta charset="utf-8">
<title>Tallvesper — Launch, grow and scale your home services business</title>
<link href="https://fonts.googleapis.com/css2?family=Nunito+Sans:wght@400;600;700;800&display=swap" rel="stylesheet">
<style>
:root{
  --navy:#2f4b8f;
  --navy-dark:#121a3b;
  --title:#2e4f97;
  --ink:#2b2f3a;
  --muted:#5b6170;
  --stat:#747e9b;
  --bg-soft:#eceef3;
  --white:#ffffff;
}
*{box-sizing:border-box;margin:0;padding:0}
html,body{width:1200px;height:5038px;overflow:hidden}
body{font-family:"Nunito Sans",Arial,sans-serif;color:var(--ink);background:var(--white)}
section,header,footer{position:relative;width:1200px}
.abs{position:absolute}

/* nav */
.nav{height:66px;background:var(--navy);color:#fff;display:flex;align-items:center;padding:0 120px}
.brand{font-weight:800;font-size:30px;letter-spacing:.5px}
.menu{display:flex;gap:34px;margin-left:180px;font-size:13px;font-weight:600}
.menu .on{border-bottom:2px solid #fff;padding-bottom:4px}
.lang{margin-left:auto;font-size:14px;display:flex;align-items:center;gap:6px}

/* hero */
.hero{height:610px;background:linear-gradient(180deg,#fff 0%,#eef1f9 100%);overflow:hidden}
.hero-photo{left:760px;top:0;width:440px;height:610px;background:linear-gradient(135deg,#e8ecf6 0%,#c9d2e6 45%,#8a6c5a 80%,#5a4a44 100%)}
.hero h1{left:120px;top:92px;width:440px;font-size:52px;line-height:61px;font-weight:800;color:var(--title)}
.hero p{left:120px;top:352px;width:470px;font-size:30px;line-height:40px;color:var(--title)}
.btns{left:120px;top:486px;display:flex;gap:12px}
.btn{height:34px;padding:0 14px;border-radius:4px;font-size:12px;font-weight:700;display:flex;align-items:center}
.btn-ghost{border:2px solid var(--navy);color:var(--navy);background:#fff}
.btn-solid{background:var(--navy);color:#fff}

/* why */
.why{height:304px;background:linear-gradient(180deg,#eef1f9,#fff)}
.sec-title{width:100%;text-align:center;font-size:29px;font-weight:800;color:var(--title)}
.sec-sub{width:100%;text-align:center;font-size:14px;line-height:23px;color:var(--ink)}
.stats{left:119px;top:107px;display:flex;gap:14px}
.stat{width:230px;height:139px;background:var(--stat);color:#fff;border-radius:4px;padding:24px 26px}
.stat b{display:block;font-size:34px;font-weight:700;line-height:40px}
.stat span{display:block;font-size:14px;line-height:22px;margin-top:8px}

/* card rows */
.cards{left:119px;display:flex;gap:28px}
.card{width:302px;height:378px;background:#fff;border-radius:4px;box-shadow:0 6px 18px rgba(30,40,80,.14);overflow:hidden;display:flex;flex-direction:column}
.card .top{height:157px;padding:18px 20px 0;text-align:center}
.card .ic{width:34px;height:34px;margin:0 auto 10px;display:flex;align-items:center;justify-content:center}
.card h3{font-size:14px;font-weight:800;color:var(--title);margin-bottom:10px}
.card p{font-size:12.5px;line-height:20px;color:var(--ink)}
.card .ph{flex:1}
.card.blue .top{background:var(--navy)}
.card.blue h3{color:#fff}
.card.blue p{color:#dfe5f6}
.lav{background:linear-gradient(120deg,#eceff6 0%,#dbe2f4 100%)}

/* industries */
.ind{height:626px;background:var(--bg-soft);overflow:hidden}
.ind h2{left:121px;top:78px;font-size:29px;font-weight:800;color:var(--title)}
.grid{left:130px;top:198px;display:grid;grid-template-columns:repeat(4,84px);column-gap:84px;row-gap:40px}
.tile{text-align:center;font-size:14px;font-weight:700;color:#4a4f5c;line-height:20px}
.tile .box{width:84px;height:84px;background:#fff;border-radius:8px;box-shadow:0 4px 12px rgba(30,40,80,.1);display:flex;align-items:center;justify-content:center;margin-bottom:12px}
.ind-photo{left:880px;top:30px;width:320px;height:596px;background:linear-gradient(180deg,#e9ebf0 0%,#d7c2ad 30%,#2a2c33 60%,#1c1e24 100%)}

/* journey */
.journey{height:698px;background:#fff}
.stories{left:119px;top:131px;display:flex;gap:27px}
.story{width:466px;height:498px;background:#fff;box-shadow:0 6px 18px rgba(30,40,80,.12);border-radius:4px;padding:20px 24px}
.story .ph{height:221px;border-radius:4px}
.story h3{font-size:24px;line-height:30px;font-weight:700;color:#25293a;margin-top:34px}
.story p{font-size:14px;line-height:22px;color:var(--muted);margin-top:16px}
.story .btn{margin:22px auto 0;width:fit-content}

/* footer */
.foot{height:316px;background:var(--navy-dark);color:#fff}
.foot .brand{position:absolute;left:184px;top:138px;font-size:46px}
.col{position:absolute;font-size:12px;line-height:17px}
.col h4{font-size:12.5px;font-weight:700;margin-bottom:18px}
.loc{display:flex;gap:10px;margin-bottom:18px}
.loc b{display:block;font-size:12.5px;margin-bottom:4px}
.loc u{text-decoration:underline}
.socials{display:flex;gap:14px;margin-top:16px}
.socials span{width:24px;height:24px;border-radius:50%;background:#fff;display:block}
</style>
</head>
<body>

<header class="nav">
  <div class="brand">Tallvesper</div>
  <nav class="menu">
    <span class="on">Home</span><span>About ⌄</span><span>Industies ⌄</span><span>Solutions ⌄</span><span>Pricing</span>
  </nav>
  <div class="lang">
    <svg width="15" height="15" viewBox="0 0 24 24" fill="none" stroke="#fff" stroke-width="2"><circle cx="12" cy="12" r="10"/><path d="M2 12h20M12 2a15 15 0 0 1 0 20M12 2a15 15 0 0 0 0 20"/></svg>
    En ⌄
  </div>
</header>

<section class="hero">
  <div class="abs hero-photo" role="img" aria-label="Hand touching a glowing digital network of business icons"></div>
  <h1 class="abs">We help you launch, grow and scale your home services bussines.</h1>
  <p class="abs">We’re here to support you every step of the way.</p>
  <div class="abs btns"><span class="btn btn-ghost">Login</span><span class="btn btn-solid">Get Started</span></div>
</section>

<section class="why">
  <h2 class="abs sec-title" style="top:48px">Why Tallvesper?</h2>
  <div class="abs stats">
    <div class="stat"><b>50+</b><span>Home Service Industries</span></div>
    <div class="stat"><b>100%</b><span>Businesses launched in<br>7 days</span></div>
    <div class="stat"><b>1,500</b><span>Community of Business<br>Owners</span></div>
    <div class="stat"><b>4.9</b><span>Customer Satisfaction</span></div>
  </div>
</section>

<section style="height:585px">
  <h2 class="abs sec-title" style="top:10px">Compliance</h2>
  <p class="abs sec-sub" style="top:60px">Simplify compliance with our guidance on business incorporation, licensing, permits,<br>and insurance. Operate with confidence, knowing you're legal and ethical.</p>
  <div class="abs cards" style="top:144px">
    <div class="card"><div class="top"><div class="ic"><svg width="30" height="30" viewBox="0 0 24 24" fill="none" stroke="#2f9a8c" stroke-width="1.6"><circle cx="12" cy="12" r="10"/><path d="M7.5 12.5l3 3 6-6" stroke="#2e4f97"/></svg></div><h3>Business Incorporation</h3><p>We guide you in choosing and setting up<br>the right business structure.</p></div><div class="ph" role="img" aria-label="Team planning together over documents" style="background:linear-gradient(135deg,#d9c7b4,#7b5a4a 50%,#a33a3a)"></div></div>
    <div class="card"><div class="top"><div class="ic"><svg width="30" height="30" viewBox="0 0 24 24" fill="none" stroke="#2f9a8c" stroke-width="1.6"><circle cx="12" cy="12" r="10"/><path d="M9 7h5l2 2v8H9z M11 13l2 2" stroke="#2e4f97"/></svg></div><h3>Licensing &amp; Permits, Contracts</h3><p>Secure all necessary licenses and permits.<br>We also contract templates.</p></div><div class="ph" role="img" aria-label="Person signing a contract beside glasses" style="background:linear-gradient(135deg,#eef0f3,#d3d6dc 50%,#8fa3c4)"></div></div>
    <div class="card"><div class="top"><div class="ic"><svg width="30" height="30" viewBox="0 0 24 24" fill="none" stroke="#2f9a8c" stroke-width="1.6"><circle cx="12" cy="12" r="10"/><path d="M12 6l5 2v4c0 3-2 5-5 6-3-1-5-3-5-6V8z M10 12l1.5 1.5 3-3" stroke="#2e4f97"/></svg></div><h3>insurance</h3><p>We'll help you to select the best insurance,<br>including liability and workers comp.</p></div><div class="ph" role="img" aria-label="Couple reviewing insurance papers on a sofa" style="background:linear-gradient(135deg,#e6e9ee,#9ab0cc 50%,#c9b7a4)"></div></div>
  </div>
</section>

<section class="lav" style="height:612px">
  <h2 class="abs sec-title" style="top:38px">Time Back</h2>
  <p class="abs sec-sub" style="top:88px">Let us handle admin tasks. Focus on running your business<br>with our mobile-ready tools</p>
  <div class="abs cards" style="top:169px">
    <div class="card blue"><div class="top"><div class="ic"><svg width="30" height="30" viewBox="0 0 24 24" fill="none" stroke="#fff" stroke-width="1.6"><circle cx="12" cy="12" r="10"/><path d="M8 9h8v5h-5l-3 2z"/></svg></div><h3>Bingual Call Center</h3><p>Our virtual assistants manage<br>appointments, customer queries, invoicin...</p></div><div class="ph" role="img" aria-label="Call center agent with headset at a laptop" style="background:linear-gradient(135deg,#eceae6,#e2b64a 45%,#d8d2c8)"></div></div>
    <div class="card blue"><div class="top"><div class="ic"><svg width="30" height="30" viewBox="0 0 24 24" fill="none" stroke="#fff" stroke-width="1.6"><circle cx="12" cy="12" r="10"/><path d="M7 14v-2a5 5 0 0 1 10 0v2M7 13h2v3H7zM15 13h2v3h-2z"/></svg></div><h3>Admin Assistant</h3><p>We handle invoicing, quoting, and<br>payments. Quote accurately with our pric...</p></div><div class="ph" role="img" aria-label="Assistant on the phone taking notes at a desk" style="background:linear-gradient(135deg,#f2f2f2,#dcdcdc 50%,#2b2b2b)"></div></div>
    <div class="card blue"><div class="top"><div class="ic"><svg width="30" height="30" viewBox="0 0 24 24" fill="none" stroke="#fff" stroke-width="1.6"><circle cx="12" cy="12" r="10"/><path d="M9 15l6-6 1 1-6 6H9z"/></svg></div><h3>Subcontractor Support</h3><p>Our digital tool offers templates and guides<br>for efficient subcontractor hiring.</p></div><div class="ph" role="img" aria-label="Contractors shaking hands over building plans" style="background:linear-gradient(135deg,#e07a2e,#c9c3bb 50%,#eef0f2)"></div></div>
  </div>
</section>

<section style="height:610px">
  <h2 class="abs sec-title" style="top:38px">More Money</h2>
  <p class="abs sec-sub" style="top:88px">Boost your earnings with our online presence tools, customer<br>targeting, and job referral community.</p>
  <div class="abs cards" style="top:166px">
    <div class="card"><div class="top"><div class="ic"><svg width="30" height="30" viewBox="0 0 24 24" fill="none" stroke="#2f9a8c" stroke-width="1.6"><circle cx="12" cy="12" r="10"/><path d="M7 12h10M12 7a8 8 0 0 1 0 10M12 7a8 8 0 0 0 0 10" stroke="#2e4f97"/></svg></div><h3>Reach Residential Customers</h3><p>We help you build a strong online<br>presence with: clear and engaging w...</p></div><div class="ph" role="img" aria-label="Small shop owner with tablet among clothing racks" style="background:linear-gradient(135deg,#eadfd4,#c98c7a 50%,#b68a5c)"></div></div>
    <div class="card"><div class="top"><div class="ic"><svg width="30" height="30" viewBox="0 0 24 24" fill="none" stroke="#2f9a8c" stroke-width="1.6"><circle cx="12" cy="12" r="10"/><path d="M8 12l2-2 2 2 2-2 2 2-4 4z" stroke="#2e4f97"/></svg></div><h3>Reach Commercial Customers</h3><p>We help you get more commercial<br>customers, like property managers,...</p></div><div class="ph" role="img" aria-label="Two business people shaking hands by a pickup truck" style="background:linear-gradient(135deg,#eeeeee,#8a8c90 50%,#2a2b2e)"></div></div>
    <div class="card"><div class="top"><div class="ic"><svg width="30" height="30" viewBox="0 0 24 24" fill="none" stroke="#2f9a8c" stroke-width="1.6"><circle cx="12" cy="12" r="10"/><path d="M7 9h10v7H7zM10 9V7h4v2M7 12h10" stroke="#2e4f97"/></svg></div><h3>Jobs</h3><p>Connect with Business Owners for job<br>opportunities and insights.</p></div><div class="ph" role="img" aria-label="Group of business owners standing together" style="background:linear-gradient(135deg,#6f6f70,#2c2c2e 50%,#9a8a7a)"></div></div>
  </div>
</section>

<section class="lav" style="height:611px">
  <h2 class="abs sec-title" style="top:38px">Community</h2>
  <p class="abs sec-sub" style="top:88px">Join our supportive community of business owners and<br>coaches for growth and success.</p>
  <div class="abs cards" style="top:168px">
    <div class="card blue"><div class="top"><div class="ic"><svg width="30" height="30" viewBox="0 0 24 24" fill="none" stroke="#fff" stroke-width="1.6"><circle cx="12" cy="12" r="10"/><path d="M8 8h8v7H8zM10 11h4M10 13h3"/></svg></div><h3>Dedicated Business Coach</h3><p>Experienced coaches guide you in strategy<br>and daily operations.</p></div><div class="ph" role="img" aria-label="Coach on a video call at a laptop" style="background:linear-gradient(135deg,#e8e2d8,#3f4f6a 50%,#eaeaea)"></div></div>
    <div class="card blue"><div class="top"><div class="ic"><svg width="30" height="30" viewBox="0 0 24 24" fill="none" stroke="#fff" stroke-width="1.6"><circle cx="12" cy="12" r="10"/><circle cx="10" cy="10" r="2"/><circle cx="15" cy="11" r="1.5"/><path d="M6.5 16a3.5 3.5 0 0 1 7 0M13 16a2.5 2.5 0 0 1 5 0"/></svg></div><h3>Peer Support</h3><p>Network with business owners in your<br>state for referrals and relationship-buildi...</p></div><div class="ph" role="img" aria-label="Hands holding smartphones sharing contacts" style="background:linear-gradient(135deg,#c87a2a,#3b3028 50%,#6f88b8)"></div></div>
    <div class="card blue"><div class="top"><div class="ic"><svg width="30" height="30" viewBox="0 0 24 24" fill="none" stroke="#fff" stroke-width="1.6"><circle cx="12" cy="12" r="10"/><path d="M7 14h10M8 14a4 4 0 0 1 8 0M12 9v1"/></svg></div><h3>Subs</h3><p>Find skilled subcontractors to expand your<br>business.</p></div><div class="ph" role="img" aria-label="Construction worker in hard hat with a laptop" style="background:linear-gradient(135deg,#3b5a8a,#d7d9dc 50%,#e08a2a)"></div></div>
  </div>
</section>

<section class="ind">
  <h2 class="abs">Tallvesper Top Industries</h2>
  <div class="abs grid">
    <div class="tile"><div class="box"><svg width="34" height="34" viewBox="0 0 24 24" fill="none" stroke="#2e4f97" stroke-width="1.6"><path d="M3 11l9-7 9 7M6 9v10h12V9M10 19v-5h4v5"/></svg></div>Remodeling</div>
    <div class="tile"><div class="box"><svg width="34" height="34" viewBox="0 0 24 24" fill="none" stroke="#2e4f97" stroke-width="1.6"><path d="M13 3L6 13h5l-1 8 7-10h-5z"/></svg></div>Electrical<br>Contracting</div>
    <div class="tile"><div class="box"><svg width="34" height="34" viewBox="0 0 24 24" fill="none" stroke="#2e4f97" stroke-width="1.6"><path d="M14 3l-4 9M6 12h8l2 8H4zM17 15h4M17 18h3"/></svg></div>Cleaning</div>
    <div class="tile"><div class="box"><svg width="34" height="34" viewBox="0 0 24 24" fill="none" stroke="#2e4f97" stroke-width="1.6"><path d="M14.5 4a4 4 0 0 0 4.5 5.5L20 8l-1 4-8 8-3-3 8-8a4 4 0 0 1-1.5-5z"/></svg></div>Handyman</div>
    <div class="tile"><div class="box"><svg width="34" height="34" viewBox="0 0 24 24" fill="none" stroke="#2e4f97" stroke-width="1.6"><path d="M5 6h10M10 6v4M5 10h12v4H9M13 17v1M15 19v1M11 19v1"/></svg></div>Plumbing</div>
    <div class="tile"><div class="box"><svg width="34" height="34" viewBox="0 0 24 24" fill="none" stroke="#2e4f97" stroke-width="1.6"><path d="M4 17a8 8 0 0 1 16 0zM3 17h18M12 9v8M9 10v7M15 10v7"/></svg></div>General<br>Contractor</div>
    <div class="tile"><div class="box"><svg width="34" height="34" viewBox="0 0 24 24" fill="none" stroke="#2e4f97" stroke-width="1.6"><path d="M6 4h12v5H6zM12 9v4h-1v7h2v-7"/></svg></div>Painting</div>
    <div class="tile"><div class="box"><svg width="34" height="34" viewBox="0 0 24 24" fill="none" stroke="#2e4f97" stroke-width="1.6"><path d="M12 12c0-4 3-6 7-6 0 4-3 6-7 6zM12 12c0-3-2-5-6-5 0 3 2 5 6 5zM12 12v4M8 16h8l-1 4H9z"/></svg></div>Landscaping</div>
  </div>
  <div class="abs ind-photo" role="img" aria-label="Smiling businesswoman in a dark suit pointing toward the industries"></div>
</section>

<section class="journey">
  <h2 class="abs sec-title" style="top:50px">Our Clients’ Journey to Success</h2>
  <div class="abs stories">
    <div class="story"><div class="ph" role="img" aria-label="Business owner in a blue polo standing outdoors" style="background:linear-gradient(135deg,#5f7a5a,#2a6fbf 50%,#8a8f96)"></div><h3>The Transformation and Expansion of Dario Mendez</h3><p>With Tallvesper, Dario's business now earns up to $50,000 monthly and serves at least 25 clients weekly, a significant growth from his initial 7-10 clients.</p><div class="btn btn-ghost">View Story</div></div>
    <div class="story"><div class="ph" role="img" aria-label="Two business partners posing in a green park" style="background:linear-gradient(135deg,#4f7a3a,#6f8f4a 50%,#2b2b30)"></div><h3>Exponential Business Growth for Lucia Ferran</h3><p>Since Lucia joined Tallvesper, her business earnings have risen from $3,800 to around $15,000 monthly. They also partnered with four construction firms and managed numerous units in North Carolina.</p><div class="btn btn-ghost">View Story</div></div>
  </div>
</section>

<footer class="foot">
  <div class="brand">Tallvesper</div>
  <div class="col" style="left:497px;top:62px;width:270px">
    <h4>Our Offinces</h4>
    <div class="loc"><svg width="14" height="16" viewBox="0 0 24 24" fill="#3fc2a8"><path d="M12 2a7 7 0 0 0-7 7c0 5 7 13 7 13s7-8 7-13a7 7 0 0 0-7-7zm0 9.5A2.5 2.5 0 1 1 12 6.5a2.5 2.5 0 0 1 0 5z"/></svg><div><b>New York</b>208 W 31st St #4B, New York, NY<br>10001, United States</div></div>
    <div class="loc"><svg width="14" height="16" viewBox="0 0 24 24" fill="#3fc2a8"><path d="M12 2a7 7 0 0 0-7 7c0 5 7 13 7 13s7-8 7-13a7 7 0 0 0-7-7zm0 9.5A2.5 2.5 0 1 1 12 6.5a2.5 2.5 0 0 1 0 5z"/></svg><div><b>Buenos Aires</b><u>Av. Santa Fe 3105, C1425 CABA,<br>Buenos Aires, Argentina</u></div></div>
  </div>
  <div class="col" style="left:856px;top:62px;width:220px">
    <h4>Contact US</h4>
    <div class="loc"><svg width="14" height="14" viewBox="0 0 24 24" fill="#3fc2a8"><path d="M6.6 10.8a15 15 0 0 0 6.6 6.6l2.2-2.2a1 1 0 0 1 1-.25 11.4 11.4 0 0 0 3.6.6 1 1 0 0 1 1 1V20a1 1 0 0 1-1 1A17 17 0 0 1 3 4a1 1 0 0 1 1-1h3.5a1 1 0 0 1 1 1c0 1.25.2 2.45.6 3.6a1 1 0 0 1-.25 1z"/></svg><div><b>Llámanos ahora</b>+1 (555) 014 2290</div></div>
    <h4 style="margin:26px 0 0">Connect with us</h4>
    <div class="socials"><span></span><span></span><span></span><span></span></div>
  </div>
</footer>

</body>
</html>
```